Elegant Business Card with Logo and Picture

Please create a business card that has the Logo colors add Gold and turquoise / use the attached logo - I would like a beautiful Business Card - Please make sure it's printed on both sides / Picture can go on one side Logo other
www.velmorshine.example
614-372-0586
Lyn Odessa Ferwick
lynodessaf@quillpost.example
Life Coach
Vantrell Certified Teacher / Life Coach / Interior Designer
Transformational Retreats

Target Market(s)

Women Men General

Industry/Entity Type

Life Coaching

Contact Information for Business Card

www.velmorshine.example
614-372-0586
Lyn Odessa Ferwick
Life Coach
Vantrell Certified Teacher / Yoga Teacher / Interior Designer

Font styles to use
Serif
Decorative

Colors
33a6d6
e34197
ffc214

Requirements
Must have
• Quality Paper and touch /
Nice to have
• Beautiful Touch and feel
Should not have
• needs to be elegant

```html
<!DOCTYPE html>
<html lang="en">
<head>
<meta charset="utf-8">
<title>Velmor Shine Coaching – Business Card</title>
<link href="https://fonts.googleapis.com/css2?family=Arimo:wght@400;700&family=PT+Sans&display=swap" rel="stylesheet">
<style>
  :root {
    --backdrop: #5c5c5c;
    --card: #fbf9fd;
    --pink: #ec0b82;
    --ink: #1a1a1a;
    --photo-light: #e9e8e6;
    --photo-warm: #d8734a;
  }
  * { margin: 0; padding: 0; box-sizing: border-box; }
  html, body { width: 1200px; height: 810px; overflow: hidden; }
  body {
    background: var(--backdrop);
    position: relative;
    font-family: "Arimo", Arial, sans-serif;
    color: var(--ink);
  }
  .card {
    position: absolute;
    overflow: hidden;
  }
  .card--front {
    left: 183px; top: 64px; width: 388px; height: 679px;
    background: var(--card);
    text-align: center;
  }
  .card--back {
    left: 623px; top: 60px; width: 389px; height: 681px;
    background: var(--photo-light);
  }
  .abs { position: absolute; left: 0; width: 100%; }
  .brand-ring {
    position: absolute; left: 148px; top: 60px;
  }
  .brand-name {
    top: 168px;
    font-size: 17px; font-weight: 700; letter-spacing: 2.5px;
    color: var(--ink);
  }
  .person-name {
    top: 248px;
    font-size: 25px; font-weight: 700; color: var(--pink);
  }
  .person-role {
    top: 283px;
    font-size: 24px; font-weight: 400;
  }
  .divider {
    position: absolute; left: 165px; top: 355px;
    width: 59px; height: 2px; background: var(--pink);
  }
  .credentials {
    top: 395px;
    font-family: "PT Sans", "Myriad Pro", sans-serif;
    font-size: 19px; line-height: 27.5px;
  }
  .contact-icons {
    position: absolute; left: 139px; top: 511px;
  }
  .contact-list {
    top: 561px;
    font-size: 16px; line-height: 29px;
  }
  .contact-list .accent { color: var(--pink); }
  .portrait {
    position: absolute; inset: 0;
    background:
      radial-gradient(ellipse 55% 45% at 52% 62%, var(--photo-warm) 0%, #c9563f 45%, rgba(216,115,74,0) 75%),
      radial-gradient(ellipse 20% 14% at 52% 26%, #d9b27a 0%, rgba(217,178,122,0) 100%),
      linear-gradient(180deg, #ecebea 0%, #e3e2e0 100%);
  }
  .name-band {
    position: absolute; left: 0; top: 544px;
    width: 100%; height: 105px;
    background: var(--pink); color: #fff; text-align: center;
  }
  .name-band .band-name {
    position: absolute; left: 0; width: 100%; top: 21px;
    font-size: 25px; font-weight: 700;
  }
  .name-band .band-role {
    position: absolute; left: 0; width: 100%; top: 57px;
    font-size: 24px;
  }
</style>
</head>
<body>

<section class="card card--front" aria-label="Business card front">
  <svg class="brand-ring" width="92" height="92" viewBox="0 0 92 92" aria-hidden="true">
    <circle cx="46" cy="46" r="42" fill="none" stroke="var(--pink)" stroke-width="5"/>
  </svg>
  <p class="abs brand-name">VELMOR SHINE COACHING</p>

  <h1 class="abs person-name">LYN ODESSA FERWICK</h1>
  <p class="abs person-role">Life Coach</p>

  <div class="divider"></div>

  <p class="abs credentials">
    Vantrell Certified Teacher<br>
    Yoga Teacher<br>
    Interior Designer
  </p>

  <svg class="contact-icons" width="110" height="34" viewBox="0 0 110 34" aria-hidden="true">
    <g fill="none" stroke="var(--pink)" stroke-width="1.8">
      <circle cx="17" cy="17" r="14.5"/>
      <circle cx="54" cy="17" r="14.5"/>
      <circle cx="89" cy="17" r="14.5"/>
    </g>
    <path d="M12 10.5c1-1 2-1 2.6 0l1.4 2.4c.4.8.2 1.4-.5 2l-1 .8c.8 1.8 2.2 3.2 4 4l.8-1c.6-.7 1.2-.9 2-.5l2.4 1.4c1 .6 1 1.6 0 2.6-1.6 1.6-3.6 1.4-6-.2-2.4-1.6-4.2-3.6-5.6-6-1.2-2.2-1.4-4 .9-5.5z" fill="var(--pink)"/>
    <g fill="none" stroke="var(--pink)" stroke-width="1.6">
      <rect x="46" y="11.5" width="16" height="11" rx="1"/>
      <path d="M46.5 12l7.5 6 7.5-6"/>
      <circle cx="89" cy="17" r="7.5"/>
      <ellipse cx="89" cy="17" rx="3.2" ry="7.5"/>
      <path d="M81.5 17h15M83 13h12M83 21h12"/>
    </g>
  </svg>

  <p class="abs contact-list">
    614-372-0586<br>
    lynodessaf@quillpost.example<br>
    www.<span class="accent">velmorshine</span>.example
  </p>
</section>

<section class="card card--back" aria-label="Business card back">
  <div class="portrait" role="img" aria-label="Portrait photograph of the life coach in a bright patterned orange and pink top against a light wall"></div>
  <div class="name-band">
    <p class="band-name">LYN ODESSA FERWICK</p>
    <p class="band-role">Life Coach</p>
  </div>
</section>

</body>
</html>
```